Bright, Fun and hard to forget home inspection business card.

We need a Business card design for a new Home Inspection company. We are building a brand that is bright, fun and easy to remember.

Target Market(s)

Anyone involed in buying and selling of homes.

Industry/Entity Type

Home Inspection

Contact Information for Business Card

Colin Hartwell Owner/Inspector

Wedsite- KestrelHouseCheck.example
Phone: 253-555-0147
Email- ColinHartwell@mailbox.example
WA Lic # 4738

Requirements
Must have
• BQRV LOGO somewhere on card.

```html
<!DOCTYPE html>
<html lang="en">
<head>
<meta charset="utf-8">
<title>Kestrel House Check – Business Card</title>
<link rel="stylesheet" href="https://fonts.googleapis.com/css2?family=Open+Sans:wght@400;600&display=swap">
<style>
  :root {
    --page: #ece9e6;
    --card-white: #ffffff;
    --brand-orange: #f07a52;
    --brand-orange-deep: #e9663e;
    --accent-red: #e8322a;
    --name-orange: #ee5a24;
    --ink: #1e1e1e;
  }
  * { box-sizing: border-box; margin: 0; padding: 0; }
  html, body {
    width: 1200px; height: 1000px; overflow: hidden;
    background: var(--page);
    font-family: "Open Sans", Arial, sans-serif;
  }
  .canvas { position: relative; width: 1200px; height: 1000px; }

  .card {
    position: absolute; left: 265px; width: 665px; height: 397px;
    border-radius: 26px; overflow: hidden;
    box-shadow: 0 4px 14px rgba(0,0,0,0.25);
  }
  .card--front { top: 73px; background: var(--card-white); }
  .card--back { top: 533px; background: var(--brand-orange); }

  .front-swoosh { position: absolute; inset: 0; width: 665px; height: 397px; }

  .holder { position: absolute; left: 26px; top: 126px; }
  .holder__name {
    color: var(--name-orange); font-size: 18px; font-weight: 400;
    text-transform: uppercase; letter-spacing: 0.2px;
  }
  .holder__title { color: var(--ink); font-size: 15px; margin-left: 77px; margin-top: -2px; }

  .contact { position: absolute; left: 26px; top: 250px; color: var(--ink); font-size: 15px; }
  .contact__licence { margin-bottom: 6px; }
  .contact__row { display: flex; align-items: center; gap: 7px; height: 24px; }
  .contact__icon { width: 12px; height: 12px; fill: var(--accent-red); }

  .mascot-area { position: absolute; border-radius: 18px; }
  .mascot-area--front {
    left: 292px; top: 48px; width: 150px; height: 180px;
    background: linear-gradient(160deg, #f4f1ef, #f8cdbd);
  }
  .mascot-area--back {
    left: 75px; top: 78px; width: 220px; height: 260px;
    background: var(--brand-orange-deep);
  }

  .company-name {
    position: absolute; font-family: "Open Sans", Arial, sans-serif;
    font-weight: 600; line-height: 1.15;
  }
  .company-name--front {
    left: 455px; top: 100px; width: 185px;
    font-size: 28px; color: var(--ink);
  }
  .company-name--back {
    left: 320px; top: 140px; width: 290px;
    font-size: 44px; color: var(--card-white);
  }
</style>
</head>
<body>
<main class="canvas">

  <section class="card card--front" aria-label="Business card front">
    <svg class="front-swoosh" viewBox="0 0 665 397" aria-hidden="true">
      <defs>
        <linearGradient id="swooshFill" x1="0" y1="0" x2="1" y2="0">
          <stop offset="0" stop-color="#ee4a2e"/>
          <stop offset="0.5" stop-color="#f26a4a"/>
          <stop offset="1" stop-color="#f4866a"/>
        </linearGradient>
      </defs>
      <path d="M0,372 C260,360 480,318 665,240 L665,397 L0,397 Z" fill="var(--accent-red)"/>
      <path d="M0,397 L0,390 C270,376 490,334 665,258 L665,397 Z" fill="url(#swooshFill)"/>
    </svg>

    <div class="mascot-area mascot-area--front" role="img" aria-label="Brand illustration: cartoon inspector holding a megaphone, with a small house"></div>
    <p class="company-name company-name--front">Kestrel House Check LLC</p>

    <div class="holder">
      <p class="holder__name">Colin Hartwell</p>
      <p class="holder__title">Owner/Inspector</p>
    </div>

    <div class="contact">
      <p class="contact__licence">WA Lic # 4738</p>
      <p class="contact__row">
        <svg class="contact__icon" viewBox="0 0 24 24" aria-hidden="true"><path d="M6.6 10.8a15.1 15.1 0 0 0 6.6 6.6l2.2-2.2c.3-.3.7-.4 1-.2 1.1.4 2.3.6 3.6.6.6 0 1 .4 1 1V20c0 .6-.4 1-1 1A17 17 0 0 1 3 4c0-.6.4-1 1-1h3.5c.6 0 1 .4 1 1 0 1.3.2 2.5.6 3.6.1.3 0 .7-.2 1z"/></svg>
        253-555-0147
      </p>
      <p class="contact__row">
        <svg class="contact__icon" viewBox="0 0 24 24" aria-hidden="true"><path d="M2 5h20v14H2z M3.5 6.5 12 13l8.5-6.5" stroke="#fff" stroke-width="1.6"/></svg>
        ColinHartwell@mailbox.example
      </p>
      <p class="contact__row">
        <svg class="contact__icon" viewBox="0 0 24 24" aria-hidden="true"><circle cx="12" cy="12" r="10"/><path d="M2 12h20M12 2c3 3 3 17 0 20M12 2c-3 3-3 17 0 20" stroke="#fff" stroke-width="1.4" fill="none"/></svg>
        KestrelHouseCheck.example
      </p>
    </div>
  </section>

  <section class="card card--back" aria-label="Business card back">
    <div class="mascot-area mascot-area--back" role="img" aria-label="Brand illustration: cartoon inspector holding a megaphone, with a small house"></div>
    <p class="company-name company-name--back">Kestrel House Check LLC</p>
  </section>

</main>
</body>
</html>
```